Window Cleaning Flyer targeting Shopfronts and Small Commercial Work

Single page flyer similar to the flyer targeting small commercial work and shopfronts

Please include the following text:

Brisk Pane Services delivers high quality service to suburbs all around Melbourne. From Frankston to Kalkallo, Brisk has you covered!

With over 10 years experience, Brisk specialises in providing:
- Window Cleaning: via elevated work platforms, rope access and extension poles
- Pressure Cleaning: Including chlorine treatment to prevent mould regrowth on concrete area
- Roof Gutter Cleaning: using our ladder free gutter vacuum

We pride ourselves on neat and professional presentation and vast geographical reach across Melbourne.

Our services can be completed on a frequency that meets your window cleaning needs. Whether a weekly clean or a yearly service.

Brisk Pane Services Melbourne takes care of all your window cleaning needs.

Contact Us now for free quote!

Target Market(s)

Small business and commercial building owners

Industry/Entity Type

Window Cleaning

Requirements
Must have
• Only use photos/logos provided
Should not have
• Stock phots

```html
<!DOCTYPE html>
<html lang="en">
<head>
<meta charset="utf-8">
<title>Brisk Pane Services Flyer</title>
<link href="https://fonts.googleapis.com/css2?family=Roboto+Condensed:ital,wght@0,400;0,500;0,700;1,400;1,500&display=swap" rel="stylesheet">
<style>
  :root {
    --backdrop: #231f20;
    --brand-blue: #0b6a93;
    --brand-yellow: #fff22e;
    --paper: #ffffff;
    --text-light: #ffffff;
    --photo-building: #6b5a4e;
    --photo-slats: #b49a76;
    --photo-house: #8c7565;
  }
  * { margin: 0; padding: 0; box-sizing: border-box; }
  html, body {
    width: 1200px; height: 900px; overflow: hidden;
    background: var(--backdrop);
    font-family: "Roboto Condensed", "Arial Narrow", sans-serif;
  }
  .canvas { position: relative; width: 1200px; height: 900px; }
  .flyer-art { position: absolute; left: 292.5px; top: 47px; width: 575px; height: 809px; }
  .copy { position: absolute; font-size: 12.5px; line-height: 15px; }
  .copy.light { color: var(--text-light); font-weight: 500; text-align: justify; text-align-last: left; }
  .copy.accent { color: var(--brand-yellow); font-style: italic; font-weight: 400; }
  .copy.justified { text-align: justify; text-align-last: left; }
  .brand-name {
    position: absolute; left: 362px; top: 110px; width: 210px;
    color: var(--brand-yellow); font-weight: 700; text-align: center;
    font-size: 27px; line-height: 32px; letter-spacing: 0.5px; text-transform: uppercase;
  }
  .cta { position: absolute; left: 319px; top: 733px; color: var(--brand-yellow);
         font-style: italic; font-size: 16px; font-weight: 500; line-height: 18px; }
</style>
</head>
<body>
<div class="canvas">
  <svg class="flyer-art" viewBox="312 50 613 863" xmlns="http://www.w3.org/2000/svg">
    <rect x="312" y="50" width="613" height="863" fill="var(--paper)"/>
    <polygon points="360,50 652,50 588,913 312,913 312,690" fill="var(--brand-yellow)"/>
    <polygon points="378,50 637,50 572,913 316,913" fill="var(--brand-blue)"/>
    <polygon points="637,50 925,50 925,360 862,913 572,913" fill="var(--brand-yellow)"/>
    <polygon points="890,670 925,665 925,913 862,913" fill="var(--paper)"/>
    <polygon points="652,50 906,50 872,492 620,492" fill="var(--photo-building)" role="img" aria-label="Photo: worker on an elevated platform cleaning high windows"/>
    <polygon points="618,510 748,510 765,680 857,672 843,913 588,913" fill="var(--photo-slats)" role="img" aria-label="Photo: technician using an extension pole on a slatted commercial facade"/>
    <polygon points="735,378 925,360 925,665 762,680" fill="var(--brand-yellow)"/>
    <polygon points="750,393 925,378 925,652 767,664" fill="var(--photo-house)" role="img" aria-label="Photo: technician cleaning windows of a two-storey brick building"/>
  </svg>

  <div class="brand-name">Brisk<br>Pane Services</div>

  <p class="copy light" style="left:361px; top:235px; width:196px;">Brisk Pane Services delivers high quality service to suburbs all around Melbourne. From Frankston to Kalkallo, Brisk has you covered!</p>

  <p class="copy accent" style="left:354px; top:311px; width:200px;">With over 10 years experience, Brisk specialises in providing:</p>

  <p class="copy accent" style="left:352px; top:356px; width:182px;">• Window Cleaning: via elevated work platforms, rope access and extension poles</p>

  <p class="copy accent" style="left:347px; top:417px; width:182px;">• Pressure Cleaning: Including chlorine treatment to prevent mould regrowth on concrete area</p>

  <p class="copy accent" style="left:341px; top:477px; width:182px;">• Roof Gutter Cleaning: using our ladder free gutter vacuum</p>

  <p class="copy accent justified" style="left:335px; top:523px; width:197px;">We pride ourselves on neat and professional presentation and vast geographical reach across Melbourne.</p>

  <p class="copy light" style="left:327px; top:583px; width:199px;">Our services can be completed on a frequency that meets your window cleaning needs. Whether a weekly clean or a yearly service.</p>

  <p class="copy light" style="left:321px; top:659px; width:198px;">Brisk Pane Services Melbourne takes care of all your window cleaning needs.</p>

  <p class="cta">Contact Us now for free quote!</p>
</div>
</body>
</html>
```